K9 Orbit needs a business card designed

We need a business card designed for K9 Orbit, an expansion of K9 Technics Pty Ltd (www.k9technics.com.au)

We provide high quality professional services for the Australian space industry. Our clients include the Southern Stellar Bureau and companies working in the space industry. We identify people with space related skills both locally and internationally who are then contracted by clients to create products and support space launch activities.

Colours to be used:
- Navy blue #000080
- Rocket metallic #8A7F8D
- Platinum #E5E4E2
- Black #000000
- White #FFFFFF

*Front of the card*
I have attached our K9 Orbit logo, which needs to be the main item on the card. The 'Space' text should be placed to the right of the 'K9' part rather than below, similar to the attached K9 Technics card, which this card should match.

If subtext is included, however, it should read ‘Labour Hire • Consultancy • Project Delivery’ rather than the ‘Design • Build • Test • Maintain’ of the K9 Technics card.

A black background (rather than blue background in the K9 Technics card) might be good, with a white pattern as in the K9 Technics card. If colour is used, the logo should be in its standard colours (as provided for the K9 Orbit logo).

*Back of the card*
Include a smaller K9 Orbit logo on the back.

We need the following details for K9 Orbit personnel (as a template for entry):
- Name
- Company Position
- Mobile Number
- Email
- Office Address
- Include the K9 Orbit website: www.k9orbit.com.au

Overall, we'd like to see a design that communicates the adventure of space, professional integrity, and customer service. We look forward to seeing what you can come up with.

Target Market(s)

We provide high quality professional services for the Australian space industry. Our clients include the Southern Stellar Bureau and companies working in the space industry.

Contact Information for Business Card

- Name
- Company Position
- Mobile Number
- Email
- Office Address

Requirements
Must have
• See project description.

```html
<!DOCTYPE html>
<html lang="en">
<head>
<meta charset="utf-8">
<title>K9 Orbit — Business Card</title>
<link href="https://fonts.googleapis.com/css2?family=Arimo:wght@400;700&display=swap" rel="stylesheet">
<style>
  :root {
    --stage: #1c1c1e;
    --card: #0b0b0c;
    --navy: #2b2b9c;
    --metal: #8a7f8d;
    --platinum: #e5e4e2;
    --white: #ffffff;
    --divider: #2a2a2d;
  }
  * { box-sizing: border-box; margin: 0; padding: 0; }
  html, body {
    width: 1200px; height: 900px; overflow: hidden;
    background: var(--stage);
    font-family: "Arimo", Arial, sans-serif;
  }
  .stage {
    position: relative; width: 1200px; height: 900px;
    display: flex; align-items: center; justify-content: center; gap: 40px;
  }
  .card {
    position: relative; width: 520px; height: 318px;
    background: var(--card); border-radius: 22px; overflow: hidden;
  }

  /* Company name set as plain text */
  .company-name {
    font-weight: 400; letter-spacing: 0; white-space: nowrap;
  }

  /* Back: contact side */
  .card-back { display: flex; }
  .back-brand {
    width: 46%; display: flex; align-items: center; justify-content: center;
    border-right: 1px solid var(--divider); margin: 28px 0;
  }
  .back-brand .company-name { color: var(--navy); font-size: 28px; }

  .contact { flex: 1; padding: 56px 24px 0 30px; color: var(--platinum); }
  .contact-name { color: var(--navy); font-weight: 700; font-size: 19px; letter-spacing: .3px; }
  .contact-role { font-size: 14px; color: var(--platinum); margin-top: 3px; }
  .contact-list { list-style: none; margin-top: 18px; }
  .contact-list li { display: flex; align-items: center; gap: 9px; font-size: 14px; line-height: 22px; }
  .contact-list svg { width: 14px; height: 14px; flex: none; }
  .web-accent { color: var(--navy); }
  .contact-address { margin-top: 16px; font-size: 14px; line-height: 19px; font-style: normal; }

  /* Front: brand side */
  .card-front { display: flex; flex-direction: column; align-items: center; justify-content: center; }
  .card-front .company-name { color: var(--white); font-size: 46px; }
  .tagline { margin-top: 28px; color: var(--metal); font-size: 15px; letter-spacing: .4px; }
</style>
</head>
<body>
<main class="stage">

  <section class="card card-back" aria-label="Card back with contact details">
    <div class="back-brand">
      <p class="company-name">K9 Orbit</p>
    </div>
    <div class="contact">
      <h1 class="contact-name">DANIEL REEVES</h1>
      <p class="contact-role">Managing Director</p>
      <ul class="contact-list">
        <li>
          <svg viewBox="0 0 14 14" fill="none" stroke="#2b2b9c" stroke-width="1.5"><rect x="3.5" y="1" width="7" height="12" rx="1.2"/><line x1="6" y1="11" x2="8" y2="11"/></svg>
          044-987 654 321
        </li>
        <li>
          <svg viewBox="0 0 14 14"><rect x="1" y="3" width="12" height="8" fill="#2b2b9c"/><polyline points="1,3 7,8 13,3" fill="none" stroke="#0b0b0c" stroke-width="1.2"/></svg>
          hello@mailhost.com
        </li>
        <li>
          <svg viewBox="0 0 14 14" fill="none" stroke="#2b2b9c" stroke-width="1.3"><circle cx="7" cy="7" r="5.8"/><ellipse cx="7" cy="7" rx="2.6" ry="5.8"/><line x1="1.2" y1="7" x2="12.8" y2="7"/><line x1="2" y1="4.2" x2="12" y2="4.2"/><line x1="2" y1="9.8" x2="12" y2="9.8"/></svg>
          <span>www.<span class="web-accent">k9orbit</span>.com.au</span>
        </li>
      </ul>
      <address class="contact-address">421, Address line goes here<br>45452, Country Name</address>
    </div>
  </section>

  <section class="card card-front" aria-label="Card front with company name">
    <p class="company-name">K9 Orbit</p>
    <p class="tagline">Labour Hire • Consultancy • Project Delivery</p>
  </section>

</main>
</body>
</html>
```